Clinvora Franchise LLC Informational Catalogue/Flipbook

We are seeking a professional, yet inviting informational catalogue/flipbook on owning a medical waste franchise with Clinvora Franchise LLC. Our vision is to print this catalogue in color, landscape orientation, spiral-bound, and about 6in x 9in in size.
For branding continuity, please refer to our website: www.clinvora-example.com.
Attached please find the text copy, organized by page, as well as a .zip folder containing photos that can be used throughout the catalogue. Not all of the photos have to be used, so chose at your own discretion.
Look and feel
Each slider illustrates characteristics of the customer's brand and the style your logo design should communicate.

```html
<!DOCTYPE html>
<html lang="en">
<head>
<meta charset="utf-8">
<title>Clinvora – Industries We Serve</title>
<link href="https://fonts.googleapis.com/css2?family=Fira+Sans+Extra+Condensed:wght@800&family=Roboto:wght@400;700&display=swap" rel="stylesheet">
<style>
  :root {
    --red-light: #e5393b;
    --red-bright: #e01f26;
    --red-dark: #a62127;
    --ink: #2f2f2f;
    --paper: #ffffff;
  }
  html, body {
    margin: 0;
    padding: 0;
    overflow: hidden;
    background: var(--paper);
  }
  .page {
    position: relative;
    width: 1200px;
    height: 800px;
    overflow: hidden;
    background: var(--paper);
    font-family: "Roboto", Arial, sans-serif;
    color: var(--ink);
  }
  .facets {
    position: absolute;
    inset: 0;
    width: 1200px;
    height: 800px;
  }
  .facet-top { fill: var(--red-light); }
  .facet-middle { fill: var(--red-bright); }
  .facet-bottom { fill: var(--red-dark); }
  .section-title {
    position: absolute;
    left: 66px;
    top: 355px;
    margin: 0;
    font-family: "Fira Sans Extra Condensed", "Arial Narrow", sans-serif;
    font-weight: 800;
    font-size: 47px;
    line-height: 44px;
    color: var(--paper);
    letter-spacing: 0.2px;
  }
  .industry-list {
    position: absolute;
    top: 114px;
    margin: 0;
    padding: 0;
    list-style: none;
    font-size: 19.5px;
    line-height: 32.6px;
    letter-spacing: 0.1px;
  }
  .industry-list--left { left: 536px; }
  .industry-list--right { left: 839px; }
  .industry-list li {
    position: relative;
    padding-left: 27px;
    white-space: nowrap;
  }
  .industry-list li::before {
    content: "»";
    position: absolute;
    left: 0;
    top: -1px;
    color: var(--red-bright);
    font-weight: 700;
    font-size: 20px;
  }
  .closing-note {
    position: absolute;
    left: 1037px;
    top: 709px;
    margin: 0;
    font-size: 19.5px;
  }
</style>
</head>
<body>
<main class="page">
  <svg class="facets" viewBox="0 0 2339 1568" preserveAspectRatio="none" aria-hidden="true">
    <polygon class="facet-top" points="0,0 610,0 853,783 0,485"/>
    <polygon class="facet-middle" points="0,485 853,783 0,1080"/>
    <polygon class="facet-bottom" points="0,1080 853,783 615,1568 0,1568"/>
  </svg>

  <h1 class="section-title">Industries<br>We Serve</h1>

  <ul class="industry-list industry-list--left">
    <li>Animal orphanages</li>
    <li>Allergists</li>
    <li>Assisted living homes</li>
    <li>Blood banks</li>
    <li>Casinos</li>
    <li>Colleges &amp; Universities</li>
    <li>Clinics</li>
    <li>Dentists</li>
    <li>Diagnostic centers</li>
    <li>Dialysis centers</li>
    <li>Doctors</li>
    <li>Outpatient surgery centers</li>
    <li>Endo center</li>
    <li>Government agencies</li>
    <li>Health centers &amp; departments</li>
    <li>Hematologists / Oncologists</li>
    <li>Hospitals</li>
  </ul>

  <ul class="industry-list industry-list--right">
    <li>Hospital satellite facilities</li>
    <li>Imaging centers</li>
    <li>Laboratories</li>
    <li>Nursing homes</li>
    <li>OB/GYN’s</li>
    <li>Oral surgeons</li>
    <li>Pediatricians</li>
    <li>Pharmaceutical</li>
    <li>manufacturers</li>
    <li>Physicians</li>
    <li>Prisons</li>
    <li>Radiology facilities</li>
    <li>Schools</li>
    <li>Tattoo parlors</li>
    <li>Testing centers</li>
    <li>Urologists</li>
    <li>Veterinarians</li>
  </ul>

  <p class="closing-note">and More!</p>
</main>
</body>
</html>
```